ZEPHIRO needs a new business card!

ZEPHIRO is a group of gaming enthusiasts who are looking for a new corporate business card.

The typeface should be modern and minimalist with attention paid to spacing between the letters and the letters 'zephiro' look relative to each other.

Should clean, crisp and minimalist - looking serious overall but with slight tweaks to the letters to make them look playful...

Black on white is fine.

Details on the card should include:
-the word 'zephiro'
-a job title (use any, for e.g. founder)
-a name (e.g. Ned Falka)
-phone number
-email address

For inspiration: http://brisket.tumblevane-cdn.example/wp-content/uploads/2013/07/mela-1.jpg

Target Market(s)

Video gaming enthusiasts

Industry/Entity Type

Business

Requirements
Must have
• Black letter on white background.
The word "zephiro"
Nice to have
• Maybe use a conservative font like Gibraltar or Helvetica and tweaking each letter individually.

You can insert normal job titles under the "zephiro" typeface
Should not have
• Should not be cartoony or childish fonts. No colors.

```html
<!DOCTYPE html>
<html lang="en">
<head>
<meta charset="utf-8">
<title>ZEPHIRO — Business Card</title>
<link rel="stylesheet" href="https://fonts.googleapis.com/css2?family=Jost:wght@700&display=swap">
<style>
  :root {
    --ink: #000000;
    --paper: #ffffff;
  }
  html, body {
    margin: 0;
    padding: 0;
    overflow: hidden;
    background: var(--paper);
  }
  .card {
    position: relative;
    width: 1200px;
    height: 667px;
    background: var(--paper);
    overflow: hidden;
    font-family: "Jost", "Futura", sans-serif;
    color: var(--ink);
  }
  .contact-line {
    position: absolute;
    left: 44px;
    top: 575px;
    margin: 0;
    font-size: 17px;
    line-height: 1;
    font-weight: 700;
    letter-spacing: 0;
    text-transform: uppercase;
    white-space: nowrap;
  }
  .contact-line .sep {
    margin: 0 0.3em;
  }
  .wordmark {
    position: absolute;
    left: 602px;
    top: 451px;
    margin: 0;
    font-size: 178px;
    line-height: 1;
    font-weight: 700;
    letter-spacing: -0.02em;
    white-space: nowrap;
  }
</style>
</head>
<body>
  <main class="card">
    <p class="contact-line">
      <span class="name">Ned Falka</span><span class="sep">·</span><span class="role">Founder</span><span class="sep">·</span><span class="phone">+00 000 0000</span><span class="sep">·</span><span class="email">mail@zephiro.com</span>
    </p>
    <h1 class="wordmark">zephiro</h1>
  </main>
</body>
</html>
```